Business Card Design

I am a Building Surveyor and run my own Building Consultat company, providing professional advice and services to builders, architects, designers, owners, etc.

Industry/Entity Type

Business

Contact Information for Business Card

Dorwen Halket BBldgSurv (Hons)
Managing Director

57 Quillon Rise, Marrick Heights WA 6148
Mobile 0438 271 594
Email Dorwen.halket@tarnwellpq.com

Requirements
Must have
• I would like the back of the business card to be one colour (a shade of either black or maroon, matching the colours of my logo). Positioned in the centre on the back of the business card is to be my logo.

The front of the card is to be white, with my contact information in either black or maroon. The ADBldgSurv after my name should be in a smaller font size than my name. I would also like a small logo somewhere on this side of the card.

```html
<!DOCTYPE html>
<html lang="en">
<head>
<meta charset="utf-8">
<title>Tarnwell Building Consultants – Business Card</title>
<link href="https://fonts.googleapis.com/css2?family=Jura:wght@500;600&display=swap" rel="stylesheet">
<style>
  :root {
    --stage: #e9e7e4;
    --card-white: #ffffff;
    --card-black: #0e0e0f;
    --card-black-sheen: #2a2a2c;
    --maroon: #7a2c27;
    --charcoal: #3b3b3d;
    --rule: #b9b4b2;
    --back-mark: #55575a;
  }
  * { box-sizing: border-box; margin: 0; padding: 0; }
  html, body { width: 1200px; height: 1200px; overflow: hidden; }
  body {
    background: var(--stage);
    font-family: "Jura", "Trebuchet MS", sans-serif;
    position: relative;
  }
  .card {
    position: absolute;
    width: 700px;
    height: 400px;
    box-shadow: 0 10px 30px rgba(0,0,0,0.18);
  }
  /* Back side */
  .card-back {
    left: 400px; top: 130px;
    background: linear-gradient(115deg, var(--card-black) 0%, var(--card-black) 35%, var(--card-black-sheen) 55%, var(--card-black) 80%);
    display: flex; align-items: center; justify-content: center;
  }
  .brand { display: flex; align-items: center; gap: 16px; }
  .brand-dot {
    width: 62px; height: 62px; border-radius: 50%;
    background: var(--maroon);
    flex-shrink: 0;
  }
  .brand-words { display: flex; flex-direction: column; }
  .brand-name {
    font-weight: 600; letter-spacing: 3px; text-transform: uppercase;
    font-size: 38px; line-height: 1;
  }
  .brand-sub {
    font-weight: 600; letter-spacing: 2px; text-transform: uppercase;
    font-size: 13px; margin-top: 6px; padding-top: 5px;
    border-top: 1px solid currentColor; align-self: flex-end;
  }
  .card-back .brand-words { color: var(--back-mark); }

  /* Front side */
  .card-front { left: 100px; top: 640px; background: var(--card-white); }
  .card-front .brand { position: absolute; left: 30px; top: 26px; gap: 10px; }
  .card-front .brand-dot { width: 40px; height: 40px; }
  .card-front .brand-words { color: var(--charcoal); }
  .card-front .brand-name { font-size: 26px; letter-spacing: 2px; }
  .card-front .brand-sub { font-size: 9px; letter-spacing: 1.5px; margin-top: 4px; padding-top: 3px; }

  .holder { position: absolute; right: 40px; top: 120px; text-align: right; }
  .holder-name {
    color: var(--maroon); font-weight: 600; font-size: 34px; letter-spacing: 2.5px;
    line-height: 1;
  }
  .holder-title {
    color: var(--maroon); font-weight: 600; font-size: 11px; letter-spacing: 1.5px;
    margin-top: 6px; padding-top: 4px; border-top: 1px solid var(--rule);
  }
  .contacts {
    position: absolute; left: 330px; top: 225px;
    list-style: none; color: var(--maroon);
    font-weight: 600; font-size: 16px; letter-spacing: 2px;
  }
  .contacts li { display: flex; align-items: flex-start; gap: 14px; margin-bottom: 12px; line-height: 1.25; }
  .contacts svg { width: 18px; height: 18px; flex-shrink: 0; fill: var(--maroon); margin-top: 1px; }
</style>
</head>
<body>

<section class="card card-back" aria-label="Back of business card">
  <div class="brand">
    <span class="brand-dot"></span>
    <div class="brand-words">
      <span class="brand-name">Tarnwell</span>
      <span class="brand-sub">Building Consultants</span>
    </div>
  </div>
</section>

<section class="card card-front" aria-label="Front of business card">
  <div class="brand">
    <span class="brand-dot"></span>
    <div class="brand-words">
      <span class="brand-name">Tarnwell</span>
      <span class="brand-sub">Building Consultants</span>
    </div>
  </div>

  <div class="holder">
    <p class="holder-name">Dorwen Halket</p>
    <p class="holder-title">ADBldgSurv Director</p>
  </div>

  <ul class="contacts">
    <li>
      <svg viewBox="0 0 20 20" aria-hidden="true"><path d="M10 2 1 10h3v8h5v-5h2v5h5v-8h3z"/></svg>
      <span>57 Quillon Rise, Marrick Heights<br>WA 6148</span>
    </li>
    <li>
      <svg viewBox="0 0 20 20" aria-hidden="true"><path d="M6 1h8a1 1 0 0 1 1 1v16a1 1 0 0 1-1 1H6a1 1 0 0 1-1-1V2a1 1 0 0 1 1-1zm1 3v7h6V4zm3 10a1.3 1.3 0 1 0 0 2.6A1.3 1.3 0 0 0 10 14z"/></svg>
      <span>0438 271 594</span>
    </li>
    <li>
      <svg viewBox="0 0 20 20" aria-hidden="true"><path d="M1 4h18v12H1zm2 2v.3l7 5 7-5V6zm0 2.8V14h14V8.8l-7 5z"/></svg>
      <span>Dorwen.halket@tarnwellpq.com</span>
    </li>
  </ul>
</section>

</body>
</html>
```